Business card for plumber

I need a business card for my plumbing company.
on it should:
Surname
position
E-mail
Telephone & mobile phone
Website
Please everything as placeholders / fantasy names.
We stand for high quality, hygiene and professionalism.

Colours:
# 606060 anthracite
# f7931e orange
# 2b89cc blue

Industry/Entity Type

Plumber

Contact Information for Business Card

folgt...

```html
<!DOCTYPE html>
<html lang="en">
<head>
<meta charset="utf-8">
<title>Kellberg Haustechnik – Business Card</title>
<link href="https://fonts.googleapis.com/css2?family=Montserrat:wght@400;500;700&display=swap" rel="stylesheet">
<style>
  :root {
    --anthracite: #606060;
    --orange: #f7931e;
    --blue: #2b89cc;
    --card: #1c1c1d;
    --ink: #ffffff;
    --stage: #d9d9d9;
  }
  * { box-sizing: border-box; margin: 0; padding: 0; }
  html, body { width: 1186px; height: 1200px; overflow: hidden; }
  body {
    background: var(--stage);
    font-family: "Montserrat", Arial, sans-serif;
    color: var(--ink);
    position: relative;
  }
  .card {
    position: absolute;
    left: 93px;
    width: 1000px;
    height: 555px;
    background: var(--card);
    overflow: hidden;
    box-shadow: 0 6px 18px rgba(0,0,0,0.25);
  }
  .card--front { top: 30px; }
  .card--back  { top: 615px; }

  /* front */
  .wordmark { position: absolute; left: 42px; top: 62px; color: var(--blue); font-weight: 700; line-height: 1; }
  .wordmark__main { font-size: 60px; letter-spacing: 0.5px; display: block; }
  .wordmark__sub { font-size: 30px; letter-spacing: 15px; display: block; margin-top: 6px; }

  .name-band { position: absolute; left: 0; top: 240px; width: 520px; height: 94px; }
  .name-band svg { position: absolute; inset: 0; }
  .name-band__name { position: absolute; left: 43px; top: 11px; font-size: 32px; font-weight: 700; }
  .name-band__role { position: absolute; left: 43px; top: 54px; font-size: 22px; font-weight: 400; }

  .contact { position: absolute; left: 43px; top: 384px; list-style: none; }
  .contact li { display: flex; align-items: center; font-size: 24px; font-weight: 500; height: 38px; }
  .contact svg { width: 24px; height: 24px; margin-right: 12px; fill: var(--orange); flex: none; }

  /* back */
  .brand { position: absolute; right: 40px; top: 290px; display: flex; align-items: center; gap: 22px; }
  .brand__square { width: 84px; height: 84px; border: 5px solid var(--anthracite); }
  .brand__name { color: var(--blue); font-weight: 700; line-height: 1; }
  .brand__main { font-size: 58px; display: block; }
  .brand__sub { font-size: 29px; letter-spacing: 14px; display: block; margin-top: 6px; }

  .services { position: absolute; right: 40px; top: 440px; font-size: 23px; font-weight: 500; white-space: nowrap; }
  .services .dot { color: var(--orange); margin: 0 6px 0 10px; }
  .services .dot:first-child { margin-left: 0; }
</style>
</head>
<body>
  <section class="card card--front" aria-label="Business card front">
    <div class="wordmark">
      <span class="wordmark__main">KELLBERG</span>
      <span class="wordmark__sub">HAUSTECHNIK</span>
    </div>

    <div class="name-band">
      <svg viewBox="0 0 520 94" width="520" height="94" aria-hidden="true">
        <polygon points="0,0 435,0 520,86 0,86" fill="var(--blue)"/>
        <rect x="0" y="88" width="520" height="5" fill="var(--orange)"/>
      </svg>
      <span class="name-band__name">LUKAS BRENNER</span>
      <span class="name-band__role">Co-Founder</span>
    </div>

    <ul class="contact">
      <li>
        <svg viewBox="0 0 24 24" aria-hidden="true"><path d="M3 9c0-3 4-5 9-5s9 2 9 5v2h-5V9c-1-.6-2.4-1-4-1s-3 .4-4 1v2H3zM6 13h12l2 7H4z"/></svg>
        201-555-0148
      </li>
      <li>
        <svg viewBox="0 0 24 24" aria-hidden="true"><path d="M7 1h10a2 2 0 0 1 2 2v18a2 2 0 0 1-2 2H7a2 2 0 0 1-2-2V3a2 2 0 0 1 2-2zm0 3v14h10V4zm5 15.5a1.2 1.2 0 1 0 0 2.4 1.2 1.2 0 0 0 0-2.4z"/></svg>
        201-555-0193
      </li>
      <li>
        <svg viewBox="0 0 24 24" aria-hidden="true"><path d="M2 5h20v14H2zm2 2v.5l8 6 8-6V7zm0 3v7h16v-7l-8 6z"/></svg>
        info@kellberghaustechnik.com
      </li>
      <li>
        <svg viewBox="0 0 24 24" aria-hidden="true"><circle cx="12" cy="12" r="10"/><path d="M2 12h20M12 2c3 3 3 17 0 20M12 2c-3 3-3 17 0 20" stroke="var(--card)" stroke-width="1.5" fill="none"/></svg>
        www.kellberghaustechnik.com
      </li>
    </ul>
  </section>

  <section class="card card--back" aria-label="Business card back">
    <div class="brand">
      <span class="brand__square" aria-hidden="true"></span>
      <div class="brand__name">
        <span class="brand__main">KELLBERG</span>
        <span class="brand__sub">HAUSTECHNIK</span>
      </div>
    </div>
    <p class="services">
      <span class="dot">•</span>Plumbing<span class="dot">•</span>Heating 24h Emergency Service<span class="dot">•</span>Maintenance
    </p>
  </section>
</body>
</html>
```